Card design for orthopaedic surgeons working as The Brindlewood Orthopaedic Centre

Business cards, letterhead

Colors

Designer to choose colors to be used in the design.

Requirements
Must have
• Late addition.
• Cards letterhead must have logos of
• Corvane Federated Institute of Surgeons
• Meridale Orthopaedic Society
Nice to have
• Back of card to have space for appointment time to be added by hand and some blank space for writing incidental other notes.

```html
<!DOCTYPE html>
<html lang="en">
<head>
<meta charset="utf-8">
<title>The Brindlewood Orthopaedic Centre – Business Cards</title>
<link rel="stylesheet" href="https://fonts.googleapis.com/css2?family=Lato:wght@400;700;900&display=swap">
<style>
  :root {
    --navy: #0b2f4a;
    --sky: #4fa6dc;
    --paper: #ffffff;
    --backdrop: #2a2a2c;
    --ink-light: #ffffff;
  }
  * { box-sizing: border-box; margin: 0; padding: 0; }
  html, body {
    width: 1200px;
    height: 900px;
    overflow: hidden;
    background: var(--backdrop);
    font-family: "Lato", sans-serif;
  }
  .canvas {
    position: relative;
    width: 1200px;
    height: 900px;
  }
  .card {
    position: absolute;
    width: 560px;
    height: 320px;
    background: var(--paper);
    border-radius: 16px;
    overflow: hidden;
    box-shadow: 0 14px 30px rgba(0,0,0,0.45);
  }
  .card--front { left: 60px; top: 100px; }
  .card--back { left: 580px; top: 480px; }

  .brand-name {
    font-family: "Lato", sans-serif;
    font-weight: 400;
    color: var(--navy);
    white-space: nowrap;
    letter-spacing: 0.2px;
  }
  .card--front .brand-name {
    position: absolute;
    left: 0; right: 0;
    top: 142px;
    text-align: center;
    font-size: 27px;
  }
  .card--back .brand-name {
    position: absolute;
    left: 34px;
    top: 60px;
    font-size: 19px;
  }

  .card-wave {
    position: absolute;
    inset: 0;
    width: 100%;
    height: 100%;
  }
  .wave-main { fill: var(--navy); }
  .wave-accent { fill: var(--sky); }

  .holder {
    position: absolute;
    right: 34px;
    top: 26px;
    text-align: right;
  }
  .holder-name {
    font-weight: 900;
    font-size: 25px;
    color: var(--navy);
    letter-spacing: 0.5px;
  }
  .holder-role {
    font-weight: 400;
    font-size: 14px;
    color: var(--sky);
    margin-top: 2px;
  }

  .contact-list {
    position: absolute;
    left: 40px;
    bottom: 26px;
    list-style: none;
    color: var(--ink-light);
    font-size: 15px;
  }
  .contact-item {
    display: flex;
    align-items: center;
    gap: 12px;
    line-height: 26px;
  }
  .contact-icon {
    width: 15px;
    height: 15px;
    flex: none;
  }
  .contact-icon * { fill: none; stroke: var(--ink-light); stroke-width: 1.6; stroke-linecap: round; stroke-linejoin: round; }
</style>
</head>
<body>
<main class="canvas">

  <section class="card card--front" aria-label="Card front">
    <p class="brand-name">The Brindlewood Orthopaedic Centre</p>
  </section>

  <section class="card card--back" aria-label="Card back">
    <svg class="card-wave" viewBox="0 0 560 320" preserveAspectRatio="none" aria-hidden="true">
      <path class="wave-accent" d="M250,172 C400,166 530,140 548,62 C556,66 560,72 560,80 L560,110 C515,160 400,168 250,172 Z"/>
      <path class="wave-main" d="M0,270 C30,195 110,176 250,172 C400,168 515,160 560,110 L560,320 L0,320 Z"/>
    </svg>

    <p class="brand-name">The Brindlewood Orthopaedic Centre</p>

    <div class="holder">
      <p class="holder-name">JOHN SMITH</p>
      <p class="holder-role">Founder &amp; CEO</p>
    </div>

    <ul class="contact-list">
      <li class="contact-item">
        <svg class="contact-icon" viewBox="0 0 16 16" aria-hidden="true">
          <path d="M3 2 L6 2 L7 5 L5.5 6.5 C6.5 8.5 7.5 9.5 9.5 10.5 L11 9 L14 10 L14 13 C14 13.6 13.6 14 13 14 C7 14 2 9 2 3 C2 2.4 2.4 2 3 2 Z"/>
        </svg>
        <span>1234567890</span>
      </li>
      <li class="contact-item">
        <svg class="contact-icon" viewBox="0 0 16 16" aria-hidden="true">
          <rect x="1.5" y="3.5" width="13" height="9" rx="1"/>
          <path d="M1.5 4 L8 9 L14.5 4"/>
        </svg>
        <span>info@yourmail.com</span>
      </li>
      <li class="contact-item">
        <svg class="contact-icon" viewBox="0 0 16 16" aria-hidden="true">
          <circle cx="8" cy="8" r="6.5"/>
          <ellipse cx="8" cy="8" rx="2.8" ry="6.5"/>
          <path d="M1.5 8 H14.5"/>
        </svg>
        <span>www.yourwebsite.com</span>
      </li>
    </ul>
  </section>

</main>
</body>
</html>
```